I have a business that exists already (Belvina Conservatory of Music) that we offer music lessons to all instruments. I recently opened a smaller version called TONES by Belvina that will only teach piano lessons. What I'm looking for now is a 3 page Website on word press. After I choose the design I like I want to be able to take over the website and bring it to our hosting company. We want full control of it and our team will take over. The reason I'm doing this is to have other visions and ideas from others. The first page will be about the company and our message/vision. Second page about the piano lessons. The third will be about franchising this concept "Tones by Belvina" Attached are 3 Logos . Please refer to our existing website www.belvinamusicschool-example.com to look at our piano page and franchising page. Please feel free to message me if you need more info. Thanks
Please note I do not want the new website (Tones by Belvina) To look like the other Website (Belvina Conservatory of Music) Fresh new look. I do not want the colours red or using the Red logo. I only provided it so that you have an Idea of What the other business looks like and that you can take the piano content and franchise content off of it. Tones by Belvina is smaller concept and only piano lessons.
Thanks
Only Piano lessons for all students
3 page

```html
<!DOCTYPE html>
<html lang="en">
<head>
<meta charset="utf-8">
<title>TONES by Belvina – Piano Lessons for Beginners</title>
<link rel="stylesheet" href="https://fonts.googleapis.com/css2?family=Jost:wght@400;500&family=Poppins:wght@300;400;500;600;700&display=swap">
<style>
:root{
  --orange:#ee7f00;
  --orange-deep:#d86f00;
  --brown:#9a5a14;
  --ink:#1b1b1b;
  --navy:#1f2b5c;
  --muted:#6f6f6f;
  --light:#f6f6f7;
  --grey-block:#dcdcdc;
  --green:#5cc23a;
  --teal:#3bb8c4;
  --red:#e0482a;
  --yellow:#f4c41c;
}
*{box-sizing:border-box;margin:0;padding:0}
html,body{width:1200px;height:4013px;overflow:hidden}
body{position:relative;font-family:"Poppins",sans-serif;color:var(--ink);background:#fff}
.abs{position:absolute}
.heading{font-family:"Jost",sans-serif;font-weight:400}

/* header */
.site-header{left:0;top:0;width:1200px;height:101px;background:var(--orange)}
.brand{left:112px;top:22px;color:#fff;font-family:"Jost",sans-serif;font-size:34px;font-weight:500;letter-spacing:1px;line-height:1}
.brand small{display:block;font-size:15px;letter-spacing:0;margin-top:4px;padding-left:26px}
.main-nav a{position:absolute;top:39px;color:#fff;font-size:13px;text-decoration:none}
.main-nav .active{font-weight:600}
.sign-in{left:972px;top:36px;color:#fff;font-size:13px;display:flex;align-items:center;gap:14px}

/* hero */
.hero{left:0;top:101px;width:1200px;height:571px;background:linear-gradient(100deg,#3a3633 0%,#5b544e 45%,#8c8277 75%,#b9ad9f 100%)}
.hero-title{left:106px;top:280px;color:#fff;font-size:47px}
.hero-text{left:107px;top:356px;width:440px;color:#fff;font-size:13px;line-height:22px}
.btn{display:flex;align-items:center;justify-content:center;background:var(--orange);color:#fff;font-size:12px;font-weight:500;letter-spacing:.5px;text-transform:uppercase}
.hero-btn{left:107px;top:428px;width:191px;height:50px}

/* intro */
.intro-title{left:105px;top:858px;font-size:37px;line-height:47px;color:var(--ink)}
.intro-text{left:105px;top:1022px;width:405px;font-size:13.5px;line-height:25px;color:var(--muted);font-weight:300}
.read-more{font-size:12px;font-weight:600;letter-spacing:.4px;text-transform:uppercase}
.intro-more{left:105px;top:1224px;color:var(--orange)}
.intro-photo{left:661px;top:773px;width:437px;height:380px;background:linear-gradient(135deg,#c9b8a8,#7c6b60 60%,#2b2422)}
.intro-splash{left:540px;top:790px;width:130px;height:300px;background:linear-gradient(180deg,#1d1d1d,#3a3a3a);border-radius:40% 10% 30% 60%}
.feature-card{left:824px;top:1003px;width:259px;height:346px;background:#fff;box-shadow:0 8px 24px rgba(0,0,0,.1)}
.feature-card li{position:absolute;left:34px;list-style:none;display:flex;gap:12px;font-size:12.5px;line-height:22px;color:var(--navy)}
.feature-card svg{margin-top:5px;flex:none}

/* banner */
.banner{left:0;top:1472px;width:1200px;height:359px;background:linear-gradient(100deg,#a7651c,#c58734 50%,#9b5b16)}
.banner-text{left:0;top:1562px;width:1200px;text-align:center;color:#fff;font-size:34px;font-weight:600;line-height:54px}

/* benefits */
.benefits-title{left:0;top:1980px;width:1200px;text-align:center;font-size:31px;line-height:46px}
.benefit{width:300px;text-align:center}
.benefit .icon{width:104px;height:104px;margin:0 auto;border-radius:50%;background:#fff;box-shadow:0 6px 18px rgba(0,0,0,.09);display:flex;align-items:center;justify-content:center}
.benefit h3{margin-top:26px;font-family:"Jost",sans-serif;font-weight:400;font-size:19px}
.benefit p{margin-top:12px;font-size:12.5px;line-height:23px;color:var(--muted);font-weight:300}
.staff-band{left:0;top:2438px;width:1200px;height:149px;background:linear-gradient(180deg,#fff,#ececee)}

/* testimonials */
.testimonials{left:0;top:2587px;width:1200px;height:711px;background:var(--light)}
.testimonials-title{left:0;top:2688px;width:1200px;text-align:center;font-size:46px}
.card-shadow{left:86px;top:2851px;width:506px;height:312px;background:var(--grey-block)}
.card{left:111px;top:2828px;width:506px;height:308px;background:#fff}
.review{width:460px}
.avatar{width:52px;height:50px;background:linear-gradient(135deg,#8b6c62,#3a2c29)}
.review .name{position:absolute;left:72px;top:4px;font-size:22px;font-weight:500;color:var(--navy)}
.review .place{position:absolute;left:72px;top:36px;font-size:13px;color:var(--muted)}
.review .quote{position:absolute;left:0;top:90px;width:450px;font-size:19.5px;line-height:31px;color:#444;font-weight:300}
.review .read-more{position:absolute;left:0;top:218px;color:var(--navy)}
.review .mark{position:absolute;left:407px;top:0}

/* cta */
.cta{left:0;top:3298px;width:1200px;height:242px;background:linear-gradient(100deg,#a8681e,#c28640 45%,#8e5414)}
.cta-title{left:117px;top:3376px;color:#fff;font-size:40px;font-weight:700;line-height:46px}
.cta-btn{left:848px;top:3389px;width:258px;height:51px}
.cta-price{left:848px;top:3462px;width:258px;text-align:center;color:#fff;font-size:13px}

/* footer */
.footer-col h4{font-size:16px;font-weight:600;color:var(--navy);letter-spacing:.3px}
.footer-col ul{list-style:none;margin-top:20px}
.footer-col li{font-size:12px;color:var(--muted);line-height:30px;font-weight:300}
.newsletter-text{left:774px;top:3683px;font-size:12px;color:var(--muted);font-weight:300}
.email{left:774px;top:3717px;width:300px;height:43px;border:1px solid #c9c9d6;border-radius:22px;overflow:hidden}
.email span{position:absolute;left:30px;top:12px;font-size:12px;color:#aaa}
.email .go{position:absolute;left:216px;top:0;width:84px;height:43px;background:#6e7694;display:flex;align-items:center;justify-content:center}
.copyright{left:774px;top:3778px;font-size:12px;color:var(--muted);font-weight:300}
.social{left:124px;top:3864px;display:flex;gap:18px}
.social i{display:block;width:13px;height:13px;border-radius:50%;background:var(--navy)}
.footer-keys{left:0;top:3848px;width:1200px;height:165px;background:linear-gradient(180deg,#fff 0%,#efeff2 55%,#e2e2e6 100%)}
</style>
</head>
<body>

<header class="abs site-header">
  <div class="abs brand">TONES<small>by Belvina</small></div>
  <nav class="main-nav">
    <a class="active" style="left:530px" href="#">Home</a>
    <a style="left:603px" href="#">About the piano lessons</a>
    <a style="left:799px" href="#">About franchising</a>
  </nav>
  <div class="abs sign-in">
    <svg width="22" height="22" viewBox="0 0 22 22" fill="none" stroke="#fff" stroke-width="1.6"><circle cx="11" cy="7" r="4.5"/><path d="M3 20c1-4.5 4.5-6.5 8-6.5s7 2 8 6.5"/></svg>
    Sign in
  </div>
</header>

<section class="abs hero" role="img" aria-label="Photo of a young girl playing a piano with sheet music"></section>
<h1 class="abs heading hero-title">Piano Lessons for Beginners</h1>
<p class="abs hero-text">It provides you with interactive step-by-step piano lessons that will take you from zero to pro faster than ever.</p>
<a class="abs btn hero-btn">Start now</a>

<h2 class="abs heading intro-title">Getting started as a<br>piano beginner has never<br>been easier</h2>
<p class="abs intro-text">When you think of a piano, you probably envision black and white keys but the piano is more than those harmonious sounds created by the player. The versatility and the musicianship instilled into the player from those keys is the true magic that comes from playing piano! Starting from the grassroots, experience different methods and styles of playing piano.</p>
<a class="abs read-more intro-more">Read more &nbsp;→</a>
<div class="abs intro-splash" role="img" aria-label="Black ink splash artwork"></div>
<div class="abs intro-photo" role="img" aria-label="Photo of a young woman playing piano"></div>
<ul class="abs feature-card">
  <li style="top:31px"><svg width="16" height="16"><circle cx="8" cy="8" r="8" fill="var(--green)"/><path d="M4.5 8.2l2.3 2.3 4.6-4.6" stroke="#fff" stroke-width="1.6" fill="none"/></svg><span>Learn all the essentials<br>in 10 easy-to-follow</span></li>
  <li style="top:109px"><svg width="16" height="16"><circle cx="8" cy="8" r="8" fill="var(--green)"/><path d="M4.5 8.2l2.3 2.3 4.6-4.6" stroke="#fff" stroke-width="1.6" fill="none"/></svg><span>Start playing great<br>songs from day one</span></li>
  <li style="top:187px"><svg width="16" height="16"><circle cx="8" cy="8" r="8" fill="var(--green)"/><path d="M4.5 8.2l2.3 2.3 4.6-4.6" stroke="#fff" stroke-width="1.6" fill="none"/></svg><span>Hyper effective<br>practice</span></li>
  <li style="top:265px"><svg width="16" height="16"><circle cx="8" cy="8" r="8" fill="var(--green)"/><path d="M4.5 8.2l2.3 2.3 4.6-4.6" stroke="#fff" stroke-width="1.6" fill="none"/></svg><span>Works with any piano<br>or keyboard</span></li>
</ul>

<section class="abs banner" role="img" aria-label="Warm toned photo of hands playing piano keys"></section>
<p class="abs banner-text">With these comprehensive piano lessons<br>for beginners you will get everything you<br>need to become a true piano player.</p>

<h2 class="abs heading benefits-title">For a fraction of the cost of traditional piano lessons,<br>our piano lessons makes playing and practicing more<br>fun than ever before.</h2>
<div class="abs benefit" style="left:88px;top:2205px">
  <div class="icon"><svg width="50" height="50" viewBox="0 0 50 50" fill="none" stroke="var(--orange)" stroke-width="2"><path d="M8 22h34v8H8z"/><path d="M12 22l8-12h18l4 12"/><path d="M12 30v12M38 30v12M18 34h14"/></svg></div>
  <h3>Enhanced Lessons</h3>
  <p>Play along with professional backing<br>tracks and track your progress!</p>
</div>
<div class="abs benefit" style="left:450px;top:2205px">
  <div class="icon"><svg width="50" height="50" viewBox="0 0 50 50" fill="none" stroke="var(--orange)" stroke-width="2"><path d="M22 40h22V20H22z"/><path d="M28 20v-8h10"/><circle cx="12" cy="16" r="4"/><path d="M12 20v10l6 4M8 40l4-10"/></svg></div>
  <h3>Guided Practice</h3>
  <p>It tells you exactly what to practice<br>so you're always on the right track.</p>
</div>
<div class="abs benefit" style="left:811px;top:2205px">
  <div class="icon"><svg width="50" height="50" viewBox="0 0 50 50" fill="none" stroke="var(--orange)" stroke-width="2"><rect x="11" y="14" width="28" height="20" rx="3" transform="rotate(-30 25 24)"/><path d="M16 23l14-8M19 28l14-8"/><circle cx="39" cy="40" r="3"/><path d="M42 40V30"/></svg></div>
  <h3>Games</h3>
  <p>Deep mastery requires repetition. We<br>make it fun with games!</p>
</div>
<div class="abs staff-band" role="img" aria-label="Faint decorative music staff with notes"></div>

<section class="abs testimonials"></section>
<h2 class="abs heading testimonials-title">What people are saying about us?</h2>
<div class="abs card-shadow"></div>
<div class="abs card"></div>
<article class="abs review" style="left:146px;top:2871px">
  <div class="avatar" role="img" aria-label="Reviewer portrait"></div>
  <div class="name">Kaylee Jensen</div>
  <div class="place">USA</div>
  <svg class="mark" width="42" height="34" viewBox="0 0 42 34" fill="#c9ec8a"><path d="M0 0h17v18l-8 16H2l6-14H0zM24 0h17v18l-8 16h-7l6-14h-8z"/></svg>
  <p class="quote">"My 9 year old daughter isn't even on grade one music exam but learnt Fur Elise and another song inside one week, amazing!</p>
  <a class="read-more">Read more</a>
</article>
<article class="abs review" style="left:684px;top:2871px">
  <div class="avatar" role="img" aria-label="Reviewer portrait"></div>
  <div class="name">Mia T.</div>
  <div class="place">CA</div>
  <svg class="mark" width="42" height="34" viewBox="0 0 42 34" fill="#c9ec8a"><path d="M0 0h17v18l-8 16H2l6-14H0zM24 0h17v18l-8 16h-7l6-14h-8z"/></svg>
  <p class="quote">"I have been playing the guitar for a couple of years and I wanted to try the piano. I love that i can stop the lessons.</p>
  <a class="read-more">Read more</a>
</article>

<section class="abs cta" role="img" aria-label="Warm toned photo of a woman playing piano"></section>
<h2 class="abs cta-title">Join thousands of piano<br>beginners today!</h2>
<a class="abs btn cta-btn">Start now</a>
<p class="abs cta-price">$10.99/month only</p>

<div class="abs footer-keys" role="img" aria-label="Faint curved piano keyboard decoration"></div>
<div class="abs footer-col" style="left:124px;top:3646px"><h4>ABOUT</h4><ul><li>The team</li><li>Technology</li><li>News</li><li>Blog</li><li>White Paper</li></ul></div>
<div class="abs footer-col" style="left:287px;top:3646px"><h4>INFO</h4><ul><li>FAQs</li><li>Terms</li><li>Privacy Policy</li><li>Sitemap</li></ul></div>
<div class="abs footer-col" style="left:449px;top:3646px"><h4>SUPPORT</h4><ul><li>Contacts</li><li>Support</li></ul></div>
<div class="abs footer-col" style="left:774px;top:3646px"><h4>NEWSLETTER</h4></div>
<p class="abs newsletter-text">Get our latest news right in your mailbox</p>
<div class="abs email"><span>Email</span><div class="go"><svg width="18" height="10" viewBox="0 0 18 10" fill="none" stroke="#fff" stroke-width="1.6"><path d="M0 5h16M12 1l4 4-4 4"/></svg></div></div>
<p class="abs copyright">© 2020 Company Name. All rights reserved.</p>
<div class="abs social" aria-label="Social links"><i></i><i></i><i></i><i></i><i></i><i></i></div>

</body>
</html>
```